Business Card Design

We need a business card design for a new company based in Allen, Texas. (outside of Dallas,Texas) We offer Business Management Solutions to Entrepreneurs, as well as Corporate Businesses. Our product line offers solutions to Image, Branding, Social Media marketing, business development strategies, banking / funding solutions, just to name a few. We would like to see designs that convey strength and confidence. I have attached a sample design of our company name. Designers you may use company name as either: Vorlix or Vorlix Corporation, depending on the design layout.

Please show alternate color of Black as well.

Industry/Entity Type

Business

Contact Information for Business Card

Vorlix Corporation

2847 E. Hollowbrook Drive, STE 410
Brenford, TX 75390
Office: 555.318.7742
Fax: 555.318.7743

Dr. Miles Dunworth
Business Development Director

```html
<!DOCTYPE html>
<html lang="en">
<head>
<meta charset="utf-8">
<title>Vorlix Corporation – Business Cards</title>
<link rel="stylesheet" href="https://fonts.googleapis.com/css2?family=Arimo:wght@400&family=Open+Sans:wght@600&display=swap">
<style>
  :root {
    --bg: #e6e3de;
    --card-light: #ffffff;
    --card-dark: #0f1113;
    --card-dark-edge: #1c1f22;
    --accent: #1aa3e0;
    --logo-slate: #34444f;
    --text-light: #ffffff;
    --text-soft: #e4e6e8;
  }
  html, body {
    margin: 0;
    padding: 0;
    width: 1200px;
    height: 899px;
    overflow: hidden;
    background: var(--bg);
  }
  .canvas {
    position: relative;
    width: 1200px;
    height: 899px;
  }
  .card {
    position: absolute;
    width: 636px;
    height: 363px;
    border-radius: 20px;
    overflow: hidden;
    box-shadow: 0 4px 10px rgba(0,0,0,0.25);
  }
  .card--front { left: 122px; top: 87px; background: var(--card-dark); }
  .card--back {
    left: 464px; top: 472px; width: 637px; height: 362px;
    background: radial-gradient(ellipse at 50% 40%, var(--card-dark-edge), var(--card-dark) 75%);
  }
  .front__top {
    position: absolute; left: 0; top: 0; width: 100%; height: 182px;
    background: var(--card-light);
  }
  .front__rule {
    position: absolute; left: 0; top: 182px; width: 100%; height: 4px;
    background: var(--accent);
  }
  .front__bottom {
    position: absolute; left: 0; top: 186px; width: 100%; height: 177px;
    background: radial-gradient(ellipse at 50% 0%, var(--card-dark-edge), var(--card-dark) 80%);
  }
  .wordmark {
    position: absolute;
    font-family: "Open Sans", sans-serif;
    font-weight: 600;
    line-height: 1;
    white-space: nowrap;
    transform: translate(-50%, -50%);
    letter-spacing: -1px;
  }
  .wordmark--front { left: 318px; top: 92px; font-size: 76px; color: var(--logo-slate); }
  .wordmark--back { left: 318px; top: 182px; font-size: 84px; color: var(--text-light); }
  .company {
    position: absolute; left: 39px; top: 243px;
    font-family: "Arimo", sans-serif;
    color: var(--text-light);
  }
  .company__name { font-size: 28px; line-height: 32px; margin: 0 0 4px; font-weight: 400; }
  .company__address { font-size: 14.5px; line-height: 18px; color: var(--text-soft); margin: 0; }
  .contacts {
    position: absolute; left: 452px; top: 206px;
    list-style: none; margin: 0; padding: 0;
    font-family: "Open Sans", sans-serif; font-weight: 600;
    font-size: 17px; color: var(--text-light);
  }
  .contacts li { display: flex; align-items: center; height: 35px; }
  .contacts svg { width: 26px; height: 24px; margin-right: 10px; flex: none; }
  .back__url {
    position: absolute; left: 0; width: 100%; top: 322px;
    text-align: center;
    font-family: "Open Sans", sans-serif; font-weight: 600;
    font-size: 16px; color: var(--text-light);
  }
</style>
</head>
<body>
<main class="canvas">
  <section class="card card--front">
    <div class="front__top"></div>
    <div class="front__rule"></div>
    <div class="front__bottom"></div>
    <div class="wordmark wordmark--front">Vorlix</div>
    <div class="company">
      <h1 class="company__name">Vorlix Corporation</h1>
      <p class="company__address">2847 E. Hollowbrook Drive,<br>STE 410 Brenford, TX 75390</p>
    </div>
    <ul class="contacts">
      <li>
        <svg viewBox="0 0 26 24" aria-hidden="true"><path d="M7 2 L11 6 L8.5 9 C10 13 12 15 16 17 L19 14.5 L23 18.5 L20 22 C12 21 5 14 4 5 Z" fill="#fff"/></svg>
        555.318.7742
      </li>
      <li>
        <svg viewBox="0 0 26 24" aria-hidden="true"><rect x="8" y="1" width="11" height="22" rx="1.5" fill="none" stroke="#fff" stroke-width="2"/><rect x="10" y="4" width="7" height="9" fill="#fff"/><rect x="10" y="15" width="7" height="5" fill="#fff" opacity="0.7"/></svg>
        555.318.7743
      </li>
      <li>
        <svg viewBox="0 0 26 24" aria-hidden="true"><rect x="1" y="5" width="24" height="15" fill="#fff"/><path d="M1 5 L13 14 L25 5 M1 20 L10 12 M25 20 L16 12" stroke="#0f1113" stroke-width="1.4" fill="none"/></svg>
        @vorlixcorp.com
      </li>
      <li>
        <svg viewBox="0 0 26 24" aria-hidden="true"><g fill="none" stroke="#fff" stroke-width="1.5"><circle cx="13" cy="12" r="10"/><ellipse cx="13" cy="12" rx="4.5" ry="10"/><path d="M3 12 H23 M5 7 H21 M5 17 H21 M13 2 V22"/></g></svg>
        vorlixcorp.com
      </li>
    </ul>
  </section>

  <section class="card card--back">
    <div class="wordmark wordmark--back">Vorlix</div>
    <div class="back__url">www.vorlixcorp.com</div>
  </section>
</main>
</body>
</html>
```